Neon Lodging Offers Website looking for new design

We are a online travel discounter based around hotel accommodations in Las Vegas. We need a wordpress design that will be used as our corporate cover page, and also for the affiliate pages. The current design can be viewed at http://postweaveforum.com/clients/neonoffer/ and the final design needs to include most of the navigation components. The affiliate pages will need a space to display the booking engine, for example, as shown at http://www.qrv.travel/marcoti. Our general color scheme is red/black, and the two logos we use are attached.

Because this is a crowded niche it is extremely important that we set ourselves apart in the design. The more visually stunning and out of the box the design, the better. The site needs to look distinctively different than anything else online. Since the overall layout is very basic and does not have to provide a lot of information, it leaves a lot of flexibility in design concepts.

We realize it is a truncated timetable, which is why the increased fee for your time and guaranteed payout.

Industry/Entity Type

Travel

```html
<!DOCTYPE html>
<html lang="en">
<head>
<meta charset="utf-8">
<title>Neon Lodging Offers</title>
<link href="https://fonts.googleapis.com/css2?family=Open+Sans:wght@400;600;700&display=swap" rel="stylesheet">
<style>
:root{
  --red:#d9161c;
  --red-dark:#b50f14;
  --ink:#222;
  --muted:#666;
  --line:#ddd;
  --paper:#fff;
  --soft:#f3f3f3;
  --night:#1c1c1e;
}
*{box-sizing:border-box;margin:0;padding:0}
html,body{width:1200px;height:2232px;overflow:hidden}
body{font-family:"Open Sans",Arial,sans-serif;color:var(--ink);background:var(--paper);position:relative}
.wordmark{color:var(--red);font-weight:700;font-size:20px;display:flex;align-items:center;gap:8px}
.wordmark .dot{width:14px;height:14px;border-radius:50%;background:var(--red)}

/* header */
.site-header{height:112px;display:flex;align-items:center;padding:0 40px;border-bottom:1px solid var(--line)}
.tagline{margin-left:30px;font-size:14px;color:var(--muted);width:360px;line-height:1.4}
.main-nav{margin-left:auto;display:flex;gap:30px;font-size:15px;font-weight:600}
.main-nav a{color:var(--ink);text-decoration:none;padding-bottom:4px}
.main-nav a.active{color:var(--red);border-bottom:2px solid var(--red)}

/* hero */
.hero{position:relative;height:448px}
.hero-photo{position:absolute;inset:0;background:linear-gradient(120deg,#e9e6e2 0%,#f7f6f4 45%,#cfc8bf 100%)}
.search-panel{position:absolute;left:0;top:0;width:340px;height:448px;background:var(--paper);padding:22px 26px;box-shadow:2px 0 10px rgba(0,0,0,.15)}
.search-panel h3{color:var(--red);font-size:16px;margin-bottom:12px}
.field{margin-bottom:10px}
.field label{display:block;font-size:12px;color:var(--red);font-weight:600;margin-bottom:3px}
.field span{display:block;height:28px;border:1px solid var(--line);background:var(--soft)}
.field-row{display:flex;gap:12px}
.field-row .field{flex:1}
.btn{display:inline-block;background:var(--red);color:#fff;font-weight:700;font-size:14px;padding:8px 22px;border-radius:3px}
.search-panel .btn{float:right;margin-top:6px}
.hero-copy{position:absolute;left:790px;top:90px;color:var(--ink);font-weight:700;font-size:22px;line-height:1.7;letter-spacing:.5px}
.hero-copy .accent{color:var(--red)}

/* features */
.features{height:160px;background:var(--red);display:flex;padding:18px 60px;color:#fff}
.feature{flex:1;text-align:center;padding:0 30px}
.feature svg{width:46px;height:46px}
.feature h4{font-size:20px;margin:4px 0 6px}
.feature p{font-size:12px;line-height:1.45;opacity:.95}

/* about */
.about{height:328px;display:flex;padding:24px 40px 0}
.about-intro{width:300px}
.about-intro h2{font-size:30px;font-weight:600;margin:14px 0 12px}
.about-intro p{font-size:13px;color:var(--muted);line-height:1.6}
.packages{flex:1;margin-left:40px}
.packages h2{font-size:24px;font-weight:600;margin-bottom:14px}
.tabs{display:flex;border-bottom:2px solid var(--red);font-size:13px}
.tabs span{padding:7px 16px;color:var(--muted)}
.tabs span.active{background:var(--red);color:#fff}
.deal{display:flex;gap:20px;margin-top:16px}
.deal-photo{width:330px;height:150px;background:linear-gradient(160deg,#7fa6cf,#c9b48a 60%,#6c5a45)}
.deal-text{flex:1}
.deal-text h5{font-size:15px;margin-bottom:8px}
.deal-text p{font-size:12.5px;color:var(--muted);line-height:1.6}

/* dark band */
.deals-band{height:320px;background:var(--night);color:#fff;text-align:center;padding-top:34px}
.deals-band h2{font-size:34px;font-weight:600}
.deals-band p{font-size:14px;margin-top:8px;opacity:.85}
.hotel-strip{margin:24px 0 0;height:160px;background:linear-gradient(90deg,#2f4c78,#c58a4a 25%,#40628f 50%,#d2a35c 75%,#2b3f63)}

/* group band */
.group-band{margin-top:20px;height:140px;background:var(--red);color:#fff;display:flex;align-items:center;justify-content:center;font-size:34px;font-weight:600}

/* contact */
.contact{height:480px;display:flex;gap:40px;padding:20px 40px 0}
.contact-col{flex:1}
.contact-col h3{font-size:22px;font-weight:600;margin-bottom:14px;text-align:center}
.agent{display:flex;gap:16px;align-items:flex-start}
.agent-photo{width:150px;height:300px;background:linear-gradient(180deg,#d9d9d9,#b31217 70%)}
.agent-info{font-size:13px;line-height:1.7;padding-top:40px}
.form-row{display:flex;align-items:center;gap:10px;margin-bottom:12px;font-size:13px}
.form-row label{width:80px}
.form-row span{flex:1;height:30px;border:1px solid var(--line)}
.form-row.tall{align-items:flex-start}
.form-row.tall span{height:120px}
.contact .btn{margin-left:90px}
.quote{border:1px solid var(--line);padding:16px;font-size:13px;line-height:1.6;color:var(--muted);border-radius:4px}
.author{display:flex;align-items:center;gap:10px;margin-top:16px;font-size:13px}
.author .avatar{width:44px;height:44px;border-radius:50%;background:linear-gradient(135deg,#c9a27a,#5a3b2a)}

/* footer */
.site-footer{position:absolute;left:0;right:0;bottom:0;height:212px;border-top:1px solid var(--line);padding:40px 40px 0}
.site-footer small{display:block;margin-top:90px;font-size:11px;color:var(--muted)}
</style>
</head>
<body>

<header class="site-header">
  <div class="wordmark"><span class="dot"></span>Neon Lodging Offers</div>
  <p class="tagline">Find the best deals from thousands of hotels Guaranteed</p>
  <nav class="main-nav">
    <a class="active" href="#">HOME</a><a href="#">GROUPS</a><a href="#">SEARCH EVENTS</a><a href="#">CONTACT US</a>
  </nav>
</header>

<section class="hero">
  <div class="hero-photo" role="img" aria-label="Bright modern hotel bedroom with white bedding"></div>
  <form class="search-panel">
    <h3>Hotel Search</h3>
    <div class="field"><label>Location</label><span></span></div>
    <div class="field-row">
      <div class="field"><label>Check In</label><span></span></div>
      <div class="field"><label>Check Out</label><span></span></div>
    </div>
    <div class="field"><label>Rooms</label><span></span></div>
    <div class="field-row">
      <div class="field"><label>Adults</label><span></span></div>
      <div class="field"><label>Children</label><span></span></div>
    </div>
    <div class="field"><label>Advanced options</label><span></span></div>
    <span class="btn">Search</span>
  </form>
  <div class="hero-copy">
    <div>BOOK HOTEL ROOM</div>
    <div>2000 HOTELS AROUND THE LAS VEGAS</div>
    <div class="accent">GET 10% OFF ON EVERY BOOKING</div>
  </div>
</section>

<section class="features">
  <div class="feature">
    <svg viewBox="0 0 24 24" fill="none" stroke="#fff" stroke-width="3"><circle cx="10" cy="10" r="7"/><path d="M15 15l7 7"/></svg>
    <h4>We find more hotels</h4>
    <p>simply dummy text of the printing and typesetting industry. Lorem Ipsum has been the industry's standard dummy text ever since the 1500s.</p>
  </div>
  <div class="feature">
    <svg viewBox="0 0 24 24" fill="none" stroke="#fff" stroke-width="4"><path d="M3 13l6 6L21 5"/></svg>
    <h4>Best price guaranteed</h4>
    <p>100% free, no booking fees. We'll find you the best deal possible for your hotel.</p>
  </div>
  <div class="feature">
    <svg viewBox="0 0 24 24" fill="#fff"><path d="M12 21l-8.5-8.6A5 5 0 0 1 12 5.6a5 5 0 0 1 8.5 6.8z"/></svg>
    <h4>Travellers love us</h4>
    <p>simply dummy text of the printing and typesetting industry. Lorem Ipsum has been the industry's standard dummy text ever since the 1500s.</p>
  </div>
</section>

<section class="about">
  <div class="about-intro">
    <div class="wordmark"><span class="dot"></span>Neon Lodging Offers</div>
    <h2>About Us</h2>
    <p>Neon Lodging Offers is a Hotel Deal Provider based in Las Vegas. We help guests find great hotel rooms at wholesale prices, for any stay length, from short breaks to long group trips.</p>
  </div>
  <div class="packages">
    <h2>Find the best packages for you</h2>
    <div class="tabs"><span class="active">Deal of the Day</span><span>Most Popular</span><span>Super Saver</span><span>Trending Now</span><span>Talk</span></div>
    <div class="deal">
      <div class="deal-photo" role="img" aria-label="Las Vegas strip hotel towers under a blue sky"></div>
      <div class="deal-text">
        <h5>Deluxe Las Vegas at Coral Crown Resort 20% off your room</h5>
        <p>Book or get a hotel package booked with the 20% off your room offer at Coral Crown Resort in Las Vegas between June and February, and get 20% off your room. To get the deal, be sure to book the 20% off room rate when you reserve.</p>
      </div>
    </div>
  </div>
</section>

<section class="deals-band">
  <h2>Why not get a great hotel deal in one of these in Las Vegas?</h2>
  <p>Our price guarantee ensures you get the cheapest price online on hotels around Las Vegas</p>
  <div class="hotel-strip" role="img" aria-label="Row of Las Vegas hotel and casino buildings"></div>
</section>

<section class="group-band">Need more than one room? Contact us to save on group reservations.</section>

<section class="contact">
  <div class="contact-col">
    <h3>Contact Us Today</h3>
    <div class="agent">
      <div class="agent-photo" role="img" aria-label="Portrait of the reservations agent"></div>
      <div class="agent-info">Name: Nora L. Vance<br>Email: nora@neonlodging.example<br>Phone: (555) 014-2270</div>
    </div>
  </div>
  <div class="contact-col">
    <h3>Need Help?</h3>
    <div class="form-row"><label>Name *</label><span></span></div>
    <div class="form-row"><label>E-mail *</label><span></span></div>
    <div class="form-row"><label>Telephone</label><span></span></div>
    <div class="form-row tall"><label>Message *</label><span></span></div>
    <span class="btn">Send</span>
  </div>
  <div class="contact-col">
    <h3>Testimonials</h3>
    <p class="quote">Lorem Ipsum is simply dummy text of the printing and typesetting industry. Lorem Ipsum has been the industry's standard dummy text ever since the 1500s, when an unknown printer took a galley of type and scrambled it to make a type specimen book. It has survived not only five centuries, but also the leap into electronic typesetting, remaining essentially unchanged.</p>
    <div class="author"><span class="avatar" role="img" aria-label="Guest avatar"></span>Lena Korvath – UAE</div>
  </div>
</section>

<footer class="site-footer">
  <div class="wordmark"><span class="dot"></span>Neon Lodging Offers</div>
  <small>Powered By · neonlodging</small>
</footer>

</body>
</html>
```